Redesign retirement planner website

Provide an original design for a website. The site should introduce the retirement planner, explain the basic offerings of his services, and invite the website visitor to enter their name, phone, and email. Please provide a ready-to-publish redesign that can actually be published via a Wordpress template or other major website builder like SquareSpace or Wix. Some introductory content is attached, but feel free to add additional sections/images/blocks/copywriting and rearrange/delete sections entirely to make your design original and compelling. Feel free to pull copywriting from here but again, do not use this original design, feel free to create an entirely NEW design and layout. lynx-mango-trel (dot) sitefolio (dot) com password: 1234 -- FINAL NOTE: Do not choose a stock photo of a man for the retirement planner. This website needs to work well with no photo of the retirement planner himself. Think of a non-face-focused design to win this competition.

Industry/Entity Type

Retirement planner personal website

Number of Pages Required

1 page

Font styles to use
Sans Serif
Decorative

Requirements
Must have
• Please provide a ready-to-publish redesign that can actually be published via a Wordpress template or other major website builder.

```html
<!DOCTYPE html>
<html lang="en">
<head>
<meta charset="utf-8">
<title>Marcus Hollins — Counselor &amp; Retirement Specialist</title>
<link href="https://fonts.googleapis.com/css2?family=Gloock&family=Montserrat:wght@400;500;600&display=swap" rel="stylesheet">
<style>
:root{
  --ink:#151515;
  --paper:#f5f4f1;
  --gold:#ffc700;
  --gold-line:#8a6d12;
  --white:#ffffff;
  --field:#e8e8e8;
  --field-border:#c9c9c9;
  --muted:#8a8a8a;
  --serif:'Gloock', Georgia, serif;
  --sans:'Montserrat', Arial, sans-serif;
}
*{margin:0;padding:0;box-sizing:border-box}
html,body{width:1200px;height:3745px;overflow:hidden}
body{background:var(--ink);color:var(--white);font-family:var(--sans);position:relative}
.abs{position:absolute}

/* nav */
.brand{left:83px;top:54px;font-family:var(--sans);font-weight:600;font-size:26px;color:var(--gold)}
.nav-link{top:57px;font-size:23px;color:var(--white)}
.contact-btn{left:922px;top:49px;width:194px;height:43px;border-radius:22px;background:var(--gold);color:var(--ink);font-size:23px;font-weight:500;display:flex;align-items:center;justify-content:center;gap:6px}

/* hero */
.hero-pre{left:81px;top:182px;font-size:30px}
.hero-title{left:81px;top:226px;font-family:var(--serif);font-size:80px;line-height:95px;color:var(--gold)}
.hero-sub{left:83px;top:530px;font-size:34px;line-height:41px;width:520px}
.hero-glow{left:660px;top:150px;width:490px;height:490px;border-radius:50%;background:radial-gradient(circle,#7c73a6 0%,#3a3554 45%,rgba(21,21,21,0) 72%)}
.hero-photo{left:700px;top:290px;width:400px;height:330px;border-radius:0 0 180px 140px;background:linear-gradient(160deg,#cfd8e3 0%,#7d9cc4 40%,#2f3f66 100%)}

/* intro */
.intro{left:0;top:657px;width:1200px;height:645px;background:var(--paper);overflow:hidden}
.intro-glow{left:-260px;top:250px;width:620px;height:620px;border-radius:50%;background:radial-gradient(circle,#ffc700 0%,rgba(255,199,0,.45) 30%,rgba(245,244,241,0) 68%)}
.intro-title{left:83px;top:56px;font-family:var(--serif);font-size:52px;line-height:64px;color:var(--ink)}
.intro-body{left:83px;top:284px;width:520px;font-size:32px;line-height:41px;color:var(--ink)}

/* form */
.lead-form{left:685px;top:620px;width:431px;height:648px;background:var(--white);border-radius:16px;box-shadow:0 6px 24px rgba(0,0,0,.12);color:var(--ink)}
.form-title{position:absolute;left:24px;top:30px;font-size:32px;line-height:41px;font-weight:500}
.field{position:absolute;left:24px;width:383px;height:40px;background:var(--field);border:1px solid var(--field-border);border-radius:10px;padding:9px 13px;font-size:20px;color:var(--muted)}
.field.message{height:169px}
.say-hi{position:absolute;left:24px;top:565px;width:383px;height:52px;border-radius:26px;background:var(--gold);font-size:26px;font-weight:500;display:flex;align-items:center;justify-content:center}

/* specialities */
.spec-heading{left:83px;top:1345px;font-family:var(--serif);font-size:56px;color:var(--gold)}
.glow-left{left:-420px;top:2050px;width:900px;height:900px;border-radius:50%;background:radial-gradient(circle,rgba(255,199,0,.55) 0%,rgba(190,150,0,.25) 35%,rgba(21,21,21,0) 65%)}
.glow-corner{left:820px;top:3380px;width:760px;height:760px;border-radius:50%;background:radial-gradient(circle,rgba(255,199,0,.85) 0%,rgba(200,155,0,.45) 35%,rgba(21,21,21,0) 68%)}
.spec{left:80px;width:1036px;height:394px}
.spec-head{position:absolute;left:0;top:0;width:1036px;height:100px;border-bottom:2px solid var(--gold-line)}
.spec-title{position:absolute;bottom:-6px;font-family:var(--serif);font-size:82px;line-height:1}
.spec-num{position:absolute;bottom:2px;font-family:var(--serif);font-size:52px;line-height:1}
.spec.left .spec-title{left:0}
.spec.left .spec-num{right:-6px}
.spec.right .spec-title{right:0}
.spec.right .spec-num{left:0}
.spec-text{position:absolute;top:130px;width:620px;font-size:27px;line-height:32.5px}
.spec-photo{position:absolute;top:123px;width:349px;height:195px}
.spec.left .spec-text{left:0}
.spec.left .spec-photo{right:0}
.spec.right .spec-photo{left:0;top:140px}
.spec.right .spec-text{left:394px;top:163px;width:642px}

.photo-home{background:linear-gradient(135deg,#e9e6e1 0%,#b9b2a6 45%,#3c4863 80%,#6d5a44 100%)}
.photo-meeting{background:linear-gradient(120deg,#c9a3ae 0%,#e8e4dc 35%,#5a4b46 65%,#dcd8d0 100%)}
.photo-savings{background:linear-gradient(110deg,#d8c99e 0%,#3a4a4c 40%,#2d6b6e 70%,#b9c7c9 100%)}
.photo-policy{background:linear-gradient(130deg,#4a3226 0%,#b08a6e 40%,#d9dfe6 70%,#e6c9b4 100%)}
.photo-portfolio{background:linear-gradient(90deg,#8c6a4a 0%,#6e5238 38%,#1c1f22 40%,#15181a 100%)}

/* footer */
.footer-brand{left:80px;top:3474px;font-weight:600;font-size:26px;color:var(--gold)}
.footer-rule{left:356px;top:3490px;width:755px;height:2px;background:var(--gold-line)}
.footer-small{font-size:17px;color:var(--white)}
.social{top:3567px;width:22px;height:22px;border-radius:50%;border:2px solid var(--white)}
</style>
</head>
<body>

<!-- navigation -->
<div class="abs brand">Marcus Hollins</div>
<div class="abs nav-link" style="left:527px">Home</div>
<div class="abs nav-link" style="left:639px">Specialities</div>
<div class="abs nav-link" style="left:810px">About</div>
<div class="abs contact-btn">
  <svg width="20" height="20" viewBox="0 0 24 24" aria-hidden="true"><path fill="#151515" d="M6.6 10.8c1.4 2.8 3.8 5.1 6.6 6.6l2.2-2.2c.3-.3.7-.4 1-.2 1.1.4 2.3.6 3.6.6.6 0 1 .4 1 1V20c0 .6-.4 1-1 1C10.6 21 3 13.4 3 4c0-.6.4-1 1-1h3.5c.6 0 1 .4 1 1 0 1.3.2 2.5.6 3.6.1.3 0 .7-.2 1L6.6 10.8z"/></svg>
  Contact Me
</div>

<!-- hero -->
<div class="abs hero-glow"></div>
<div class="abs hero-photo" role="img" aria-label="Photo of a retired couple relaxing together and reading a newspaper"></div>
<div class="abs hero-pre">I’m a</div>
<h1 class="abs hero-title">Counselor &amp;<br>Retirement<br>Specialist</h1>
<p class="abs hero-sub">With a unique apporach to financial planning.</p>

<!-- introduction -->
<section class="abs intro">
  <div class="abs intro-glow"></div>
  <h2 class="abs intro-title">Allow me to<br>introduce<br>myself</h2>
  <p class="abs intro-body">Your lifetime of achievements deserves the best plan. I’m honored to help you maximize your wealth for your health, family, and legacy.</p>
</section>

<!-- contact form -->
<form class="abs lead-form">
  <div class="form-title">Lets plan a<br>golden memories</div>
  <div class="field" style="top:133px">First Name</div>
  <div class="field" style="top:190px">Last Name</div>
  <div class="field" style="top:247px">Email</div>
  <div class="field" style="top:304px">Phone Number</div>
  <div class="field message" style="top:360px">Message</div>
  <div class="say-hi">Say Hi!</div>
</form>

<!-- specialities -->
<div class="abs glow-left"></div>
<div class="abs glow-corner"></div>
<h2 class="abs spec-heading">My Specialities</h2>

<article class="abs spec left" style="top:1487px">
  <div class="spec-head"><h3 class="spec-title">Estate Planning</h3><span class="spec-num">01</span></div>
  <p class="spec-text">Ensure your legacy is protected with comprehensive estate planning. I will guide you through creating wills, trusts, and other essential documents to secure your assets for future generations, ensuring your wishes are honored.</p>
  <div class="spec-photo photo-home" role="img" aria-label="Photo of a bright family home dining and living room"></div>
</article>

<article class="abs spec right" style="top:1881px">
  <div class="spec-head"><h3 class="spec-title">Retirement Forecasting</h3><span class="spec-num">02</span></div>
  <div class="spec-photo photo-meeting" role="img" aria-label="Photo of an advisor reviewing documents with a client at a table"></div>
  <p class="spec-text">Plan for a fulfilling retirement with our expert forecasting services. I will analyze your financial situation and future needs to develop a personalized strategy, helping you achieve your retirement goals with confidence.</p>
</article>

<article class="abs spec left" style="top:2275px">
  <div class="spec-head"><h3 class="spec-title">Final Expense</h3><span class="spec-num">03</span></div>
  <p class="spec-text">Prepare for life's final expenses with peace of mind. My services help you plan for costs associated with end-of-life arrangements, alleviating financial stress for your loved ones during a difficult time.</p>
  <div class="spec-photo photo-savings" role="img" aria-label="Photo of banknotes, a calculator and a small model house"></div>
</article>

<article class="abs spec right" style="top:2669px">
  <div class="spec-head"><h3 class="spec-title">Life Insurance</h3><span class="spec-num">04</span></div>
  <div class="spec-photo photo-policy" role="img" aria-label="Photo of hands holding a tablet showing a life insurance form"></div>
  <p class="spec-text">Safeguard your family's future with tailored life insurance solutions. I provide expert advice to help you choose the right coverage, ensuring financial security for your loved ones when they need it most.</p>
</article>

<article class="abs spec left" style="top:3062px">
  <div class="spec-head"><h3 class="spec-title">Portfolio Evaluation</h3><span class="spec-num">05</span></div>
  <p class="spec-text">Maximize your investment potential with our thorough portfolio evaluation. I assess your current assets and provide strategic recommendations to enhance your financial growth and stability.</p>
  <div class="spec-photo photo-portfolio" role="img" aria-label="Photo of a phone showing a stock price chart on a wooden desk"></div>
</article>

<!-- footer -->
<div class="abs footer-brand">Marcus Hollins</div>
<div class="abs footer-rule"></div>
<div class="abs footer-small" style="left:80px;top:3568px">Hancrafted in Atlanta, GA.</div>
<div class="abs footer-small" style="left:80px;top:3615px">+40-5120-7736</div>
<div class="abs footer-small" style="left:80px;top:3650px">hello@marcushollins.com</div>
<div class="abs social" style="left:913px" aria-label="Social link"></div>
<div class="abs social" style="left:975px" aria-label="Social link"></div>
<div class="abs social" style="left:1033px" aria-label="Social link"></div>
<div class="abs social" style="left:1090px" aria-label="Social link"></div>
<div class="abs footer-small" style="right:87px;top:3650px">© 2024 Marcus Hollins. All Right Reserved</div>

</body>
</html>
```